beauty salon

providing waxing services from a home base this must include which I will provide a price list and an address

Industry/Entity Type

Beauty Salon

Font styles to use
Script

Colors

Designer to choose colors to be used in the design.

```html
<!DOCTYPE html>
<html lang="en">
<head>
<meta charset="utf-8">
<title>Maren's Haven Salon – Services</title>
<link href="https://fonts.googleapis.com/css2?family=Italianno&family=Marcellus+SC&family=Raleway:wght@500&family=Arimo&family=Montserrat:wght@800;900&display=swap" rel="stylesheet">
<style>
  :root{
    --teal:#2fbcd2;
    --teal-deep:#1fa7bf;
    --plum:#b884b6;
    --plum-text:#9a5d9b;
    --plum-soft:#c48cc3;
    --ink:#1e2230;
    --silver-1:#c9cbcf;
    --silver-2:#f4f4f5;
    --white:#ffffff;
  }
  *{box-sizing:border-box;margin:0;padding:0}
  html,body{width:1200px;height:850px;overflow:hidden;background:var(--white)}
  .flyer{position:relative;width:1200px;height:850px;overflow:hidden;
    background:linear-gradient(115deg,var(--silver-1) 0%,var(--silver-2) 38%,#dcdde0 60%,#f7f7f8 80%,var(--silver-1) 100%);}
  .backdrop{position:absolute;inset:0}
  .ornament{position:absolute;left:0;top:0}
  .salon{position:absolute;left:190px;top:204px;width:225px;text-align:center;font-family:"Raleway",sans-serif}
  .salon-name{display:flex;align-items:center;justify-content:center;gap:7px;font-size:17px;font-weight:500;color:var(--plum-text)}
  .salon-name .dot{width:9px;height:9px;border-radius:50%;background:var(--plum-text)}
  .salon-address{margin-top:10px;font-size:20px;line-height:26px;color:var(--teal)}
  .hours{position:absolute;left:190px;top:324px;font-family:"Raleway",sans-serif;font-size:19px;line-height:24.5px;color:var(--plum-soft)}
  .script{font-family:"Italianno",cursive;color:var(--ink);font-weight:400;position:absolute;white-space:nowrap}
  .services-title{left:496px;top:8px;font-size:62px}
  .list-title{font-size:58px}
  .ladies-title{left:592px;top:68px}
  .mens-title{left:950px;top:68px}
  .eye-title{left:948px;top:462px;font-size:48px}
  .price-list{position:absolute;list-style:none;font-family:"Marcellus SC",serif;color:var(--ink);font-size:19px}
  .price-list li{position:absolute;left:0;right:0;display:flex;align-items:baseline;height:24px;line-height:24px}
  .price-list .item{white-space:nowrap;letter-spacing:.5px}
  .price-list .leader{flex:1;margin:0 6px;border-bottom:2px dotted #555;transform:translateY(-5px)}
  .price-list .price{font-family:"Raleway",sans-serif;font-size:19px;font-weight:500}
  .ladies{left:500px;top:0;width:310px}
  .mens{left:860px;top:0;width:312px}
  .therapist{position:absolute;left:35px;top:716px;font-family:"Arimo",sans-serif;font-size:22px;line-height:29px;color:var(--teal);
    text-shadow:-1px 0 #2a3a45,1px 0 #2a3a45,0 -1px #2a3a45,0 1px #2a3a45}
  .therapist .phone{display:flex;align-items:center;gap:6px}
  .offer{position:absolute;left:856px;top:642px;width:320px;height:120px}
  .offer-tape{position:absolute;left:4px;top:10px;width:296px;height:52px;background:var(--plum);transform:rotate(-1.5deg)}
  .offer-figure{position:absolute;left:34px;top:0;font-family:"Montserrat",sans-serif;font-weight:900;font-size:60px;line-height:72px;color:var(--teal);letter-spacing:-1px;
    text-shadow:4px 4px 0 var(--ink)}
  .offer-figure .off{color:#ececee;-webkit-text-stroke:2px var(--ink)}
  .offer-note{position:absolute;left:6px;top:82px;font-family:"Montserrat",sans-serif;font-weight:800;font-size:22px;color:var(--teal);
    text-shadow:-1px 0 #fff,1px 0 #fff,0 -1px #fff,0 1px #fff,2px 2px 2px rgba(0,0,0,.35)}
</style>
</head>
<body>
<main class="flyer">
  <svg class="backdrop" width="1200" height="850" viewBox="0 0 1200 850" aria-hidden="true">
    <path d="M0 560 C120 470 260 470 420 560 C600 660 850 760 1200 812 L1200 850 L0 850 Z" fill="#ffffff" opacity=".9"/>
    <path d="M0 575 C120 490 260 490 420 580 C600 680 850 780 1200 830 L1200 850 L0 850 Z" fill="var(--plum)"/>
  </svg>

  <svg class="ornament" width="200" height="720" viewBox="0 0 200 720" role="img" aria-label="Flowing turquoise swirl with leaves and beaded vines along the left edge">
    <defs>
      <linearGradient id="swirlTone" x1="0" y1="0" x2="1" y2="0">
        <stop offset="0" stop-color="#2fbcd2" stop-opacity=".45"/>
        <stop offset="1" stop-color="#2fbcd2" stop-opacity="0"/>
      </linearGradient>
    </defs>
    <rect width="200" height="720" fill="url(#swirlTone)"/>
  </svg>

  <section class="salon">
    <p class="salon-name"><span class="dot"></span>Maren's Haven Salon</p>
    <p class="salon-address">12 Finch Lane<br>Brookvale</p>
  </section>

  <p class="hours">Now open:<br>Wednesday 10am – 4pm<br>Fridays 10am -7pm<br>Saturday 10am - 4pm</p>

  <h1 class="script services-title">Services:</h1>
  <h2 class="script list-title ladies-title">Lady's Waxing</h2>
  <h2 class="script list-title mens-title">Men's Waxing</h2>
  <h2 class="script eye-title">Eye Enhancement</h2>

  <ul class="price-list ladies">
    <li style="top:156px"><span class="item">Eyebrow</span><span class="leader"></span><span class="price">$8</span></li>
    <li style="top:185px"><span class="item">Upper lip</span><span class="leader"></span><span class="price">$8</span></li>
    <li style="top:214px"><span class="item">Chin</span><span class="leader"></span><span class="price">$8</span></li>
    <li style="top:247px"><span class="item">Face wax</span><span class="leader"></span><span class="price">$25</span></li>
    <li style="top:281px"><span class="item">Bikini line</span><span class="leader"></span><span class="price">$15</span></li>
    <li style="top:315px"><span class="item">G string</span><span class="leader"></span><span class="price">$20</span></li>
    <li style="top:349px"><span class="item">½ Brazilian</span><span class="leader"></span><span class="price">$30</span></li>
    <li style="top:381px"><span class="item">Full Brazilian</span><span class="leader"></span><span class="price">$40</span></li>
    <li style="top:412px"><span class="item">Half arm</span><span class="leader"></span><span class="price">$20</span></li>
    <li style="top:447px"><span class="item">Upper half arm</span><span class="leader"></span><span class="price">$20</span></li>
    <li style="top:481px"><span class="item">Full arm</span><span class="leader"></span><span class="price">$25</span></li>
    <li style="top:511px"><span class="item">Half leg</span><span class="leader"></span><span class="price">$15</span></li>
    <li style="top:542px"><span class="item">Upper leg</span><span class="leader"></span><span class="price">$20</span></li>
    <li style="top:577px"><span class="item">¾ Leg</span><span class="leader"></span><span class="price">$25</span></li>
    <li style="top:609px"><span class="item">Full leg</span><span class="leader"></span><span class="price">$35</span></li>
  </ul>

  <ul class="price-list mens">
    <li style="top:156px"><span class="item">Eyebrow</span><span class="leader"></span><span class="price">$10</span></li>
    <li style="top:185px"><span class="item">Half arm</span><span class="leader"></span><span class="price">$20</span></li>
    <li style="top:214px"><span class="item">Upper half arm</span><span class="leader"></span><span class="price">$25</span></li>
    <li style="top:247px"><span class="item">Full arm</span><span class="leader"></span><span class="price">$30</span></li>
    <li style="top:281px"><span class="item">Half leg</span><span class="leader"></span><span class="price">$25</span></li>
    <li style="top:314px"><span class="item">Full leg</span><span class="leader"></span><span class="price">$45</span></li>
    <li style="top:349px"><span class="item">Chest wax</span><span class="leader"></span><span class="price">$40</span></li>
    <li style="top:381px"><span class="item">Back wax</span><span class="leader"></span><span class="price">$35</span></li>
    <li style="top:543px"><span class="item">Eyebrow tint</span><span class="leader"></span><span class="price">$12</span></li>
    <li style="top:572px"><span class="item">Eyelash tint</span><span class="leader"></span><span class="price">$15</span></li>
  </ul>

  <aside class="offer">
    <div class="offer-tape"></div>
    <p class="offer-figure">10%<span class="off">OFF</span></p>
    <p class="offer-note">ON FIRST TREATMENT</p>
  </aside>

  <footer class="therapist">
    <p>Beauty Therapist:</p>
    <p>Maren</p>
    <p>Diploma of Beauty Therapy at Linden College</p>
    <p class="phone">
      <svg width="20" height="20" viewBox="0 0 20 20" aria-hidden="true">
        <circle cx="10" cy="10" r="8.5" fill="none" stroke="#2fbcd2" stroke-width="2"/>
        <path d="M7 5.5 L8.6 5.5 L9.3 8 L8.2 8.9 C8.8 10.3 9.7 11.2 11.1 11.8 L12 10.7 L14.5 11.4 L14.5 13 C11 13.6 6.4 9 7 5.5 Z" fill="#2fbcd2"/>
      </svg>
      0400 555 019
    </p>
  </footer>
</main>
</body>
</html>
```